International Petrochemical business needs a web design for Tessaro Desk system

We need a web design for a "Tessaro Desk" system for an international petrochemical company. The web site is used internally within the company. It is hosted by an internal department which provides government permit request service for other departments.

We would like to see designs of two pages using color light blue. (home page, internal page as attached).
Home Page:
1. Header has a background image and small animation. Header on home page can be taller than the header of the internal page.
2. Layout as attached.

Internal Page:
1. Header can use the same background image as the home page and can be shorter to utilize the page for content.
2. The blue icon behind every captions represent an icon. When user move mouse over this icon, it displays the caption in Thai language as a tooltip. This icon needs to be redesign.

The final design should communicate the followings:
- Excellent service provided system in terms of time and accurary
- Rapid growth of business via building petrochemical refinery plant

For Internal Page, the blue circle behind every captions represent an icon. When mouse over this icon, a tool tip showing the caption in Thai language is shown. Please also design this icon..

There are more feedbacks from customer as followed:

1. Banner should consists of 
    1.1 "Approved" stamp on paper
    1.2 An image of Garuda. It is used on every government documents in Thailand
    1.3 Image of petrochemical plant
2. Each menu item (Home, Permit, Search, etc) should have different colors. Drop down menu will use the same color as its parent menu item.
3. Overall tone of the web page should be light blue with background of the body the web page in white
4. "New Request" button should use green color with icon on it
5. Table header of each box in the body of the page should use dark blue background with text in white

Please kindly submit your revisions.
Thank you.

Reason: We get some late feedbacks from customers which was just updated to all designers.

• 1. Design for 1024x768 screen resolution
2. Use light blue theme
3. Background of header where the company logo is must have white background

```html
<!DOCTYPE html>
<html lang="en">
<head>
<meta charset="utf-8">
<title>Tessaro Desk</title>
<link href="https://fonts.googleapis.com/css2?family=Open+Sans:ital,wght@0,400;0,600;0,700;0,800;1,400&display=swap" rel="stylesheet">
<style>
:root{
  --page-bg:#b9dcef;
  --white:#ffffff;
  --navy:#0d4b97;
  --navy-dark:#0a3f82;
  --title:#15509c;
  --link:#1a4f9e;
  --text:#333333;
  --rule:#e4e4e4;
  --row-alt:#f7f7f7;
  --green-top:#6bb91e;
  --green-bottom:#3f8c14;
  --sky-1:#2f9fe0;
  --sky-2:#bfe4f6;
  --night:#1c3b63;
}
*{box-sizing:border-box;margin:0;padding:0}
html,body{width:885px;height:1200px;overflow:hidden}
body{background:var(--page-bg);font-family:"Open Sans",sans-serif;color:var(--text);position:relative}
a{color:var(--link)}
.site-header{position:absolute;left:65px;top:0;width:755px;height:126px;background:var(--white);box-shadow:0 2px 3px rgba(0,0,0,.12)}
.brand{position:absolute;left:14px;top:24px;display:flex;align-items:center;gap:6px;font-weight:800;font-size:17px;color:var(--navy);letter-spacing:.2px}
.brand-dot{width:26px;height:26px;border-radius:50%;background:var(--sky-1)}
.tagline{position:absolute;right:15px;top:25px;text-align:right;font-style:italic;font-size:9.6px;line-height:16px;color:var(--link)}
.main-nav{position:absolute;left:15px;top:81px;display:flex}
.main-nav a{display:block;width:87.4px;height:38px;border-top:2px solid;text-align:center;line-height:36px;font-size:12px;color:var(--text);text-decoration:none;border-right:1px solid #eee}
.main-nav a:last-child{border-right:none}
.nav-rule{position:absolute;left:15px;right:15px;top:81px;height:1px;background:#e6e6e6}
.social{position:absolute;right:15px;top:90px;display:flex;gap:6px}
.social span{width:24px;height:23px;border-radius:2px}
.banner{position:absolute;left:65px;top:126px;width:755px;height:288px;background:
  linear-gradient(180deg,rgba(255,255,255,0) 55%,rgba(28,59,99,.85) 70%,rgba(47,120,170,.7) 100%),
  radial-gradient(ellipse at 55% 40%,var(--sky-1) 0%,#8fd0f1 45%,var(--sky-2) 80%);}
.seal{position:absolute;top:348px;width:52px;height:52px;border-radius:50%;background:#e8eef2;border:2px solid #d4e2ea}
.content{position:absolute;left:65px;top:414px;width:755px;height:738px;background:var(--white);box-shadow:0 1px 3px rgba(0,0,0,.1)}
.block{position:absolute}
.block h2{font-weight:400;font-size:17.5px;color:var(--title);height:28px;line-height:22px}
table{border-collapse:collapse;width:100%;font-size:10.5px;table-layout:fixed}
th{background:var(--navy);color:var(--white);font-weight:400;text-align:left;height:29px;padding-left:10px;border-right:1px solid #2d66ad;border-top:2px solid var(--navy-dark);border-bottom:2px solid var(--navy-dark)}
th:last-child{border-right:none}
td{height:29.4px;padding-left:10px;border:1px solid var(--rule);border-top:none}
tbody tr:nth-child(odd) td{background:var(--row-alt)}
td.status{color:var(--link)}
.pager td{height:21px;background:var(--white)!important;font-size:9.5px}
.pager span{margin-right:9px}
.pager .current{display:inline-block;background:var(--navy);color:var(--white);width:9px;height:10px;line-height:10px;text-align:center;margin-right:9px}
.arr{font-size:7px;color:#555}
.new-request{position:absolute;left:385px;top:471px;width:355px;height:71px;background:linear-gradient(180deg,var(--green-top),var(--green-bottom));display:flex;align-items:center;gap:18px;padding-left:22px;color:var(--white);font-weight:700;font-size:34px;letter-spacing:.5px;text-decoration:none}
.site-footer{position:absolute;left:65px;top:1168px;width:755px;font-size:9.5px;color:#111;display:flex;justify-content:space-between}
.site-footer nav a{color:#111;text-decoration:none;margin-right:5px}
</style>
</head>
<body>
<header class="site-header">
  <div class="brand"><span class="brand-dot"></span>Norvale Petrochem</div>
  <p class="tagline">Le Lorem Ipsum est simplement du faux texte employé<br>dans la composition et la mise en</p>
  <div class="nav-rule"></div>
  <nav class="main-nav">
    <a href="#" style="border-color:#45b3e4">Home</a>
    <a href="#" style="border-color:#d9252b">Permits</a>
    <a href="#" style="border-color:#1d2a6b">Search</a>
    <a href="#" style="border-color:#4cb849">Report</a>
    <a href="#" style="border-color:#1b77a6">Admin</a>
    <a href="#" style="border-color:#9b1b1f">Help</a>
  </nav>
  <div class="social"><span style="background:#3b66b1"></span><span style="background:#1b6fae"></span><span style="background:#4fb0e6"></span></div>
</header>

<div class="banner" role="img" aria-label="Petrochemical plant at dusk reflected in water under a light blue sky"></div>
<div class="seal" style="left:66px" role="img" aria-label="Approved stamp on paper badge"></div>
<div class="seal" style="left:124px" role="img" aria-label="Government emblem badge"></div>

<main class="content">
  <section class="block" style="left:15px;top:16px;width:354px">
    <h2>New Request</h2>
    <table>
      <colgroup><col style="width:117px"><col style="width:150px"><col></colgroup>
      <thead><tr><th>Request No.</th><th>Requested Date</th><th>Branch</th></tr></thead>
      <tbody>
        <tr><td><a href="#">56-0003</a></td><td>20-4-2013</td><td class="status">GC 1</td></tr>
        <tr><td><a href="#">56-0004</a></td><td>21-4-2013</td><td class="status">GC 2</td></tr>
        <tr><td><a href="#">56-0005</a></td><td>22-4-2013</td><td class="status">GC 3</td></tr>
        <tr><td><a href="#">56-0006</a></td><td>23-4-2013</td><td class="status">GC 4</td></tr>
        <tr class="pager"><td colspan="3"><span class="arr">◀</span><span class="current">1</span><span>2</span><span>3</span><span>4 <span class="arr">▶</span></span></td></tr>
      </tbody>
    </table>
  </section>

  <section class="block" style="left:385px;top:16px;width:354px">
    <h2>My Working Request</h2>
    <table>
      <colgroup><col style="width:117px"><col style="width:110px"><col></colgroup>
      <thead><tr><th>Request No.</th><th>Requested Date</th><th>Status</th></tr></thead>
      <tbody>
        <tr><td><a href="#">22-0200</a></td><td>25-3-2013</td><td class="status">Waiting for process</td></tr>
        <tr><td><a href="#">22-0210</a></td><td>24-3-2013</td><td class="status">in progress</td></tr>
        <tr><td><a href="#">55-0300</a></td><td>18-1-2013</td><td class="status">Incomplete document</td></tr>
        <tr><td><a href="#">55-0301</a></td><td>20-1-2013</td><td class="status">Cancel Requested</td></tr>
        <tr class="pager"><td colspan="3"><span class="arr">◀</span><span class="current">1</span><span>2</span><span>3</span><span>4 <span class="arr">▶</span></span></td></tr>
      </tbody>
    </table>
  </section>

  <section class="block" style="left:15px;top:228px;width:725px">
    <h2>Expiring Permits</h2>
    <table>
      <thead><tr><th>Permit No.</th><th>Expire Date</th><th>Permit Name</th><th>Branch</th><th>Required Time (Day)</th><th>Due Date</th></tr></thead>
      <tbody>
        <tr><td><a href="#">AB56007</a></td><td>20-4-2013</td><td><a href="#">Permit Name #10</a></td><td class="status">GC 1</td><td class="status">30</td><td class="status">-40</td></tr>
        <tr><td><a href="#">BIO5502</a></td><td>21-4-2013</td><td><a href="#">Permit Name #20</a></td><td class="status">GC 2</td><td class="status">60</td><td class="status">15</td></tr>
        <tr><td><a href="#">TS34821</a></td><td>22-4-2013</td><td><a href="#">Permit Name #30</a></td><td class="status">GC 3</td><td class="status">90</td><td class="status">25</td></tr>
        <tr><td><a href="#">GD47515</a></td><td>23-4-2013</td><td><a href="#">Permit Name #40</a></td><td class="status">GC 4</td><td class="status">120</td><td class="status">-90</td></tr>
        <tr class="pager"><td colspan="6"><span class="arr">◀</span><span class="current">1</span><span>2</span><span>3</span><span>4 <span class="arr">▶</span></span></td></tr>
      </tbody>
    </table>
  </section>

  <section class="block" style="left:15px;top:444px;width:354px">
    <h2>My in Progress Requests</h2>
    <table>
      <colgroup><col style="width:117px"><col style="width:110px"><col></colgroup>
      <thead><tr><th>Request No.</th><th>Requested Date</th><th>Status</th></tr></thead>
      <tbody>
        <tr><td><a href="#">56-0003</a></td><td>20-4-2013</td><td class="status">Waiting for process</td></tr>
        <tr><td><a href="#">56-0004</a></td><td>21-4-2013</td><td class="status">in progress</td></tr>
        <tr><td><a href="#">56-0005</a></td><td>22-4-2013</td><td class="status">Incomplete document</td></tr>
        <tr><td><a href="#">56-0006</a></td><td>23-4-2013</td><td class="status">Cancel Requested</td></tr>
        <tr><td><a href="#">56-0007</a></td><td>24-4-2013</td><td class="status">In progress</td></tr>
        <tr><td><a href="#">56-0008</a></td><td>25-4-2013</td><td class="status">Cancel Requested</td></tr>
        <tr><td><a href="#">56-0009</a></td><td>25-4-2013</td><td class="status">Cancel Requested</td></tr>
        <tr class="pager"><td colspan="3"><span class="arr">◀</span><span class="current">1</span><span>2</span><span>3</span><span>4 <span class="arr">▶</span></span></td></tr>
      </tbody>
    </table>
  </section>

  <a class="new-request" href="#">
    <svg width="60" height="50" viewBox="0 0 60 50" fill="none" stroke="#fff" stroke-width="3" stroke-linejoin="round">
      <rect x="4" y="20" width="46" height="26" rx="3"/>
      <line x1="10" y1="36" x2="30" y2="36"/>
      <path d="M22 30 L44 6 L52 13 L30 37 L20 40 Z"/>
    </svg>
    NEW REQUEST
  </a>

  <section class="block" style="left:385px;top:562px;width:354px">
    <h2>Recent Completed Requests</h2>
    <table>
      <thead><tr><th>Request No.</th><th>Completed Date</th></tr></thead>
      <tbody>
        <tr><td><a href="#">22-0200</a></td><td>25-3-2013</td></tr>
        <tr><td><a href="#">22-0210</a></td><td>24-3-2013</td></tr>
        <tr><td><a href="#">55-0300</a></td><td>18-1-2013</td></tr>
        <tr class="pager"><td><span class="arr">◀</span><span class="current">1</span><span>2</span><span>3</span><span>4 <span class="arr">▶</span></span></td><td></td></tr>
      </tbody>
    </table>
  </section>
</main>

<footer class="site-footer">
  <nav><a href="#">Home</a><a href="#">Permits</a><a href="#">Search</a><a href="#">Report</a><a href="#">Admin</a><a href="#">Help</a></nav>
  <span>© Copyrights 2013 All rights Reserved</span>
</footer>
</body>
</html>
```